Business card for auto dealership

Looking for a clean modern design.
Would like attached logo incorporated

Industry/Entity Type

Car dealership

Contact Information for Business Card

Name, website, phone, cell, fax, email

```html
<!DOCTYPE html>
<html lang="en">
<head>
<meta charset="utf-8">
<title>Hollis Truck &amp; Auto Sales — Business Card</title>
<link rel="stylesheet" href="https://fonts.googleapis.com/css2?family=Roboto:wght@400;700;900&display=swap">
<style>
  :root {
    --stage: #e4e4e4;
    --card-dark: #000000;
    --card-light: #ffffff;
    --ink: #000000;
    --ink-soft: #4a4a4a;
    --paper-text: #ffffff;
  }
  * { box-sizing: border-box; margin: 0; padding: 0; }
  html, body {
    width: 1200px; height: 976px; overflow: hidden;
    background: var(--stage);
    font-family: "Roboto", Arial, sans-serif;
  }
  .stage { position: relative; width: 1200px; height: 976px; }
  .card {
    position: absolute; left: 270px; width: 660px; height: 378px;
    box-shadow: 0 6px 18px rgba(0,0,0,0.18);
  }
  .card--back { top: 60px; background: var(--card-dark); }
  .card--front { top: 500px; background: var(--card-light); }

  .brand { font-weight: 900; line-height: 1; }
  .brand__name { display: block; }
  .brand__tag { display: block; letter-spacing: 0.04em; text-transform: uppercase; }

  .card--back .brand {
    position: absolute; left: 0; right: 0; top: 128px;
    text-align: center; color: var(--paper-text);
  }
  .card--back .brand__name { font-size: 78px; }
  .card--back .brand__tag { font-size: 24px; margin-top: 10px; }

  .card--front .brand {
    position: absolute; left: 44px; top: 38px; color: var(--ink);
  }
  .card--front .brand__name { font-size: 60px; }
  .card--front .brand__tag { font-size: 17px; margin-top: 6px; }

  .divider {
    position: absolute; left: 44px; top: 176px; width: 410px;
    border-top: 2px solid var(--ink);
  }
  .holder {
    position: absolute; left: 470px; top: 162px;
    font-size: 24px; font-weight: 700; color: var(--ink);
  }
  .contact {
    position: absolute; left: 44px; top: 196px; list-style: none;
    color: var(--ink-soft); font-size: 19px;
  }
  .contact__item { display: flex; align-items: center; height: 29px; }
  .contact__icon { width: 16px; height: 16px; margin-right: 8px; fill: var(--ink); }
</style>
</head>
<body>
<main class="stage">
  <section class="card card--back" aria-label="Card back">
    <div class="brand">
      <span class="brand__name">Hollis</span>
      <span class="brand__tag">Truck &amp; Auto Sales</span>
    </div>
  </section>

  <section class="card card--front" aria-label="Card front">
    <div class="brand">
      <span class="brand__name">Hollis</span>
      <span class="brand__tag">Truck &amp; Auto Sales</span>
    </div>
    <div class="divider"></div>
    <p class="holder">Dana Hollis</p>
    <ul class="contact">
      <li class="contact__item">
        <svg class="contact__icon" viewBox="0 0 16 16" aria-hidden="true"><path d="M3 1l3 3-2 2c1 2 3 4 5 5l2-2 3 3-2 3C7 15 1 9 1 3z"/></svg>
        555-010-4011
      </li>
      <li class="contact__item">
        <svg class="contact__icon" viewBox="0 0 16 16" aria-hidden="true"><path d="M4 0h8a1 1 0 0 1 1 1v14a1 1 0 0 1-1 1H4a1 1 0 0 1-1-1V1a1 1 0 0 1 1-1zm1 2v10h6V2zm3 11a1 1 0 1 0 0 2 1 1 0 0 0 0-2z"/></svg>
        555-010-2140
      </li>
      <li class="contact__item">
        <svg class="contact__icon" viewBox="0 0 16 16" aria-hidden="true"><path d="M4 1h8v4H4zM1 6h14v6h-3v3H4v-3H1zm5 5v3h4v-3z"/></svg>
        555-010-1774
      </li>
      <li class="contact__item">
        <svg class="contact__icon" viewBox="0 0 16 16" aria-hidden="true"><path d="M1 3h14v10H1zm1 1.5V12h12V4.5L8 9z"/></svg>
        dana@hollisauto.com
      </li>
      <li class="contact__item">
        <svg class="contact__icon" viewBox="0 0 16 16" aria-hidden="true"><path d="M8 1a7 7 0 1 0 0 14A7 7 0 0 0 8 1zm0 1.5c.8 0 1.7 1.5 2 3.5H6c.3-2 1.2-3.5 2-3.5zM3 7h2.8v2H3zm7.2 0H13v2h-2.8zM7 7h2v2H7zm-1 3h4c-.3 2-1.2 3.5-2 3.5S6.3 12 6 10z"/></svg>
        Hollisauto.com
      </li>
    </ul>
  </section>
</main>
</body>
</html>
```